Web Site Design for new Children's Book Series

We need a new web site design that complements a new children's book series that will be available next month. The main character is named 'Mippo Zelka Otter Cat Finch' and the story lines work through bullying issues for elementary age kids. This is a new design from scratch, but we have attached a collection of artwork from the new book series that the web site design should complement.

The scope of this project is only for the design / layout of the home page and one interior page for the web site.

Additional project details including the sitemap and example content are included in the attached document: 'Mippo Zelka Web Site.pdf'

We are open for questions and we look forward to seeing your creativity!
Updates

We have marked the project as guaranteed now!  We look forward to seeing your ideas and concepts!

Target Market(s)

Currently, there are two children’s books in the Mippo Zelka series aimed at elementary aged children. This collection is planned to grow over time. The goal of the web site is to provide information about the authors and the book series to elementary aged children (ages 3 to 12), their parents, and their school teachers and counselors.

Industry/Entity Type

Interior

Requirements
Must have
• The web site design should complement the attached artwork from the Mippo Zelka series. Overall, a full width design is desired that utilizes and open layout with lots of color.

The Mippo Zelka animal logo should be prominently placed. It is not necessary to retain the white background behind the logo.

The web site will be implemented as a responsive design using the Quill Scaffold framework and a standard 12 column grid.
Nice to have
• There are two themes in the books which should be incorporated into the web site design:

- Mippo Zelka uses the phrase “Way Cool” in describing various characters in the book and it is meant to build confidence and self esteem ... "you are way cool"

- An eagle feather is left behind as in “Zelka was here”. This eagle feature should be incorporated into the design in various locations.

```html
<!DOCTYPE html>
<html lang="en">
<head>
<meta charset="utf-8">
<title>Mippo Zelka</title>
<link href="https://fonts.googleapis.com/css2?family=Open+Sans:ital,wght@0,400;0,600;0,700;0,800;1,400;1,600&display=swap" rel="stylesheet">
<style>
:root{
  --wood-dark:#3b1f12;
  --wood-mid:#5a3220;
  --wood-light:#6e4029;
  --panel:#e4e4e4;
  --nav-green:#5ea21c;
  --nav-green-dark:#3f7a10;
  --logo-teal:#2a9d77;
  --book-teal:#2c8f8c;
  --news-red:#b0262a;
  --news-border:#8a2a2a;
  --orange:#e49a00;
  --purple:#8e1a93;
  --green-title:#5c9d1b;
  --grass-light:#8fd64e;
  --grass-dark:#3a921f;
  --footer-teal:#2aa39a;
  --ink:#222;
  --white:#fff;
}
*{box-sizing:border-box;margin:0;padding:0}
html,body{width:748px;height:1200px;overflow:hidden}
body{font-family:"Open Sans",Arial,sans-serif;color:var(--ink);position:relative;
  background:linear-gradient(90deg,var(--wood-dark),var(--wood-mid) 20%,var(--wood-light) 50%,var(--wood-mid) 80%,var(--wood-dark))}
.abs{position:absolute}
.wood{inset:0;background:repeating-linear-gradient(90deg,transparent 0 46px,rgba(0,0,0,.18) 46px 48px)}
.logo{top:20px;left:0;width:748px;text-align:center;font-weight:800;font-size:50px;letter-spacing:3px;color:var(--logo-teal);text-transform:uppercase;line-height:56px}
.panel{left:116px;top:132px;width:514px;height:1000px;background:var(--panel)}
.nav{left:84px;top:92px;width:580px;height:40px;background:var(--nav-green);border-top:2px solid #8cc640;box-shadow:0 2px 3px rgba(0,0,0,.4);text-align:center;padding-top:3px}
.nav-tail{top:112px;width:40px;height:28px;background:var(--nav-green-dark)}
.nav-tail.left{left:58px;clip-path:polygon(0 40%,100% 0,100% 100%,0 100%,30% 70%)}
.nav-tail.right{left:650px;clip-path:polygon(0 0,100% 40%,70% 70%,100% 100%,0 100%)}
.nav ul{list-style:none;font-size:8.5px;font-weight:600;color:var(--white);text-transform:uppercase;line-height:16px}
.nav li{display:inline}
.nav li+li::before{content:"|";margin:0 9px}
.book-cover{left:164px;top:165px;width:208px;height:378px;border:4px solid #3aa6a0;background:linear-gradient(180deg,#e99b79 0%,#4f8f6d 35%,#6c6a5c 55%,#4eb2ad 75%,#3d9f9a 100%);box-shadow:0 3px 6px rgba(0,0,0,.4)}
.cover-title{position:absolute;left:0;right:0;bottom:40px;text-align:center;color:#f4c6b0;font-weight:800;font-size:17px;line-height:20px;text-transform:uppercase}
.cover-authors{position:absolute;left:0;right:0;bottom:14px;text-align:center;font-size:10px;font-weight:700;font-style:italic;color:#333}
.book-page{left:372px;top:165px;width:215px;height:378px;background:linear-gradient(90deg,#cfd3d3,#f6f7f7 12%,#fff);border-right:4px solid #3aa6a0;box-shadow:0 3px 6px rgba(0,0,0,.4);padding:12px 14px 0 18px;color:var(--book-teal);font-style:italic;font-size:8.4px;line-height:12.3px;text-align:justify}
.book-page p+p{margin-top:36px}
.section-title{font-size:11.5px;font-weight:700;text-transform:uppercase}
.news-title{left:143px;top:630px;color:var(--news-red)}
.news-box{left:143px;top:650px;width:208px;height:397px;background:var(--white);border:1px solid var(--news-border);border-radius:3px;padding:6px;font-size:6.6px;line-height:8.6px;text-align:justify;overflow:hidden}
.news-box p{margin-bottom:8px}
.divider{left:377px;top:630px;width:2px;height:415px;background:#666}
.col{left:400px;width:211px}
.newsletter-title{top:630px;color:var(--orange)}
.field{display:flex;align-items:center;justify-content:flex-end;gap:5px;font-size:10.5px;font-weight:700;margin-bottom:6px}
.field span{color:var(--orange)}
.field i{display:block;width:142px;height:18px;background:var(--white);border:1px solid var(--orange);border-radius:3px}
.form-1{top:656px}
.btn{display:block;margin-left:auto;width:60px;height:16px;border-radius:3px;font-size:7px;font-weight:700;text-align:center;line-height:16px;color:#222}
.btn.orange{background:var(--orange);border:1px solid #9b6a00}
.btn.green{background:var(--green-title);border:1px solid #3d6e0d}
.rule{height:2px;background:#666}
.rule-1{top:745px}
.rule-2{top:865px}
.visits-title{top:772px;color:var(--purple)}
.visits-text{top:798px;font-size:8.5px;font-weight:600;line-height:12px;color:var(--purple)}
.newsletter2-title{top:882px;color:var(--green-title)}
.message{left:400px;top:902px;width:172px;height:95px;background:var(--white);border:1px solid var(--green-title);border-radius:3px}
.form-2{top:1008px}
.form-2 .field span{color:var(--green-title)}
.form-2 .field i{border-color:var(--green-title)}
.grass{left:0;top:1062px;width:748px;height:76px;background:linear-gradient(180deg,var(--grass-light),var(--grass-dark))}
.footer{left:0;top:1138px;width:748px;height:62px;background:var(--footer-teal)}
</style>
</head>
<body>
<div class="abs wood"></div>

<div class="abs panel"></div>

<h1 class="abs logo">Mippo Zelka</h1>

<div class="abs nav-tail left"></div>
<div class="abs nav-tail right"></div>
<nav class="abs nav">
  <ul>
    <li>Home</li><li>About the Authors</li><li>The Books</li><li>Meet the Characters</li><li>Schedule a Visit</li>
  </ul>
  <ul>
    <li>Glow and Grows</li><li>Teachable Moments</li><li>Contact Us</li><li>Blog</li>
  </ul>
</nav>

<div class="abs book-cover" role="img" aria-label="Book cover illustration: otter cat and finch characters sitting on a dock by the river">
  <div class="cover-title">Mippo Zelka<br>Otter Cat Finch</div>
  <div class="cover-authors">Nora &amp; Teodor Plaske</div>
</div>
<div class="abs book-page">
  <p>Mippo, the otter cat and Zelka, the finch, lived along the Wendle River in Marlow Bay. While playing one day, they became an unusual character named Mippo Zelka Otter Cat Finch. Mippo and Zelka travel throughout the book adjusting to their new body and learning how to use their "super powers" for good. They help kids learn how to feel good about themselves, deal with bullying, and forgiveness. A must read for young children.</p>
  <p>When the dust finally settled, Mippo and Zelka were lying on the ground, knocked out. But wait – there was something very different about them. The two of them were in one body! The front legs were Mippo's, and the rear legs were Zelka's. It was an otter cat body with fur, feathers and large wings. There were two heads on one body. One was Mippo's with whiskers and round ears, the other was Zelka's with its bright yellow beak.</p>
</div>

<h2 class="abs section-title news-title">Latest News</h2>
<div class="abs news-box">
  <p>Sed ut perspiciatis unde omnis iste natus error sit voluptatem accusantium doloremque laudantium, totam rem aperiam, eaque ipsa quae ab illo inventore veritatis et quasi architecto beatae vitae dicta sunt explicabo. Nemo enim ipsam voluptatem quia voluptas sit aspernatur aut voluptatem. Sed ut perspiciatis unde omnis iste natus error sit voluptatem accusantium doloremque laudantium, totam rem aperiam, eaque ipsa quae ab illo inventore veritatis et quasi architecto beatae vitae dicta sunt explicabo. Nemo enim ipsam voluptatem quia voluptas sit aspernatur aut voluptatem.</p>
  <p>Sed ut perspiciatis unde omnis iste natus error sit voluptatem accusantium doloremque laudantium, totam rem aperiam, eaque ipsa quae ab illo inventore veritatis et quasi architecto beatae vitae dicta sunt explicabo. Nemo enim ipsam voluptatem quia voluptas sit aspernatur aut voluptatem. Sed ut perspiciatis unde omnis iste natus error sit voluptatem accusantium doloremque laudantium, totam rem aperiam, eaque ipsa quae ab illo inventore veritatis et quasi architecto beatae vitae dicta sunt explicabo. Nemo enim ipsam voluptatem quia voluptas sit aspernatur aut voluptatem.</p>
  <p>Sed ut perspiciatis unde omnis iste natus error sit voluptatem accusantium doloremque laudantium, totam rem aperiam, eaque ipsa quae ab illo inventore.</p>
</div>

<div class="abs divider"></div>

<h2 class="abs col section-title newsletter-title">Newsletter</h2>
<div class="abs col form-1">
  <div class="field"><span>First Name</span><i></i></div>
  <div class="field"><span>Email</span><i></i></div>
  <span class="btn orange">Sign me up!</span>
</div>
<div class="abs col rule rule-1"></div>

<h2 class="abs col section-title visits-title">Author Visits</h2>
<p class="abs col visits-text">Would you like Nora and Teodor to bring Mippo and Zelka to your school?<br>Learn more here: www.MippoandZelka.example</p>
<div class="abs col rule rule-2"></div>

<h2 class="abs col section-title newsletter2-title">Newsletter</h2>
<div class="abs message"></div>
<div class="abs col form-2">
  <div class="field"><span>First Name</span><i></i></div>
  <span class="btn green">Sign me up!</span>
</div>

<div class="abs grass" role="img" aria-label="Grass illustration along the bottom of the page"></div>
<footer class="abs footer"></footer>
</body>
</html>
```